Website Redesign for Mortgage, Property and Conveyancing business

Project Overview:
We are looking for a refresh and redesign of our current website to a smart, crisp and fresh approach to Home Loans, Conveyancing and Property sales. This task will be to:
- Redesign our current website in accordance with the new wireframe.
- Provide all elements required for the design
- Build 7 key templates including:
Home Page
2nd Level Section Page
3rd level Product landing Page
2nd Level - About Us, Contact Us etc
Blog
Blog Article
Campaign Page - no header
Technical
The design is for a Wordpress website. Existing theme is Quillnest and we use Elementor for page editing. We are open to a new theme to be introduced but would prefer to stay with elementor.
Current Site is: www.corvanta.com.au
Sites that we like or elements of sites:
Pelham Real Estate: https://www.pelham-example.com.au/ (Like use of video and navigation)
Copper Lantern Lane - Mortage: https://cll-example.com.au/refinance-home-loan/ (Like landing pages a sin example)
Marquetry: https://marquetry-example.com.au/ (like Our services section).
Industry/Entity Type
Mortgage, Property, Conveyancing, Property Investment
Coding
Coded - Design and coding required
Number of Pages Required
5+ page
Font styles to use
Requirements
Must have
- Built for Wordpress and Elementor.
Nice to have
- See Project Description for links to ideas/elements that we have liked. However, open to ideas as long as the follow the navigation set out in the wire frame.

```html
<!DOCTYPE html>
<html lang="en">
<head>
<meta charset="utf-8">
<title>Brightwell – Finance, Property, Conveyancing</title>
<link href="https://fonts.googleapis.com/css2?family=Inter:wght@400;500;600;700;800&display=swap" rel="stylesheet">
<style>
:root{
  --navy:#0b3a6e;
  --navy-band:#0b3f72;
  --pink:#f0386b;
  --dark:#262626;
  --ink:#1c1c1c;
  --muted:#555;
  --white:#fff;
  --yellow:#f2d67a;
}
*{box-sizing:border-box;margin:0;padding:0}
html,body{width:1200px;height:5102px;overflow:hidden}
body{position:relative;font-family:"Inter",sans-serif;color:var(--ink);background:var(--white)}
.abs{position:absolute}
.btn{position:absolute;display:flex;align-items:center;justify-content:center;gap:12px;background:var(--pink);color:var(--white);font-weight:700;text-transform:uppercase;letter-spacing:.2px}
.photo{position:absolute}

/* hero */
.hero{position:absolute;left:0;top:0;width:1200px;height:728px;background:linear-gradient(160deg,#9aa59c 0%,#6f7a6a 35%,#4b5548 65%,#2e342c 100%)}
.brand{position:absolute;left:68px;top:40px;display:flex;align-items:center;gap:8px;background:var(--white);padding:6px 12px;font-weight:700;font-size:22px;color:var(--navy)}
.brand i{width:20px;height:20px;background:var(--navy);display:block}
.menu{position:absolute;left:1098px;top:50px;width:24px}
.menu span{display:block;height:2px;background:var(--white);margin:5px 0}
.hero h1{position:absolute;left:68px;top:494px;font-size:54px;line-height:57px;font-weight:600;color:var(--white);letter-spacing:-1px}
.hero p{position:absolute;left:68px;top:620px;font-size:24px;line-height:27px;font-weight:600;color:var(--white);letter-spacing:-.5px}
.hero .btn{left:888px;top:604px;width:246px;height:68px;border-radius:34px;font-size:20px}

/* services */
.eyebrow{font-size:15px;font-weight:700;color:var(--navy);letter-spacing:.4px}
.svc-mark{position:absolute;left:118px;top:950px;width:184px;height:186px;display:flex;flex-direction:column;align-items:center;justify-content:center;gap:12px;border:1px solid #e3e8ef}
.svc-mark i{width:56px;height:56px;background:var(--navy);display:block}
.svc-mark b{font-size:24px;color:var(--navy);font-weight:700}
.svc h2{position:absolute;left:470px;top:870px;font-size:52px;line-height:54px;font-weight:600;color:var(--navy);letter-spacing:-1px}
.find{position:absolute;left:470px;top:1034px;width:376px;height:32px;border-bottom:2px solid var(--navy);font-size:12px;color:#333;display:flex;justify-content:space-between;align-items:flex-start}
.card-img{position:absolute;top:1118px;height:376px}
.card-title{position:absolute;top:1544px;font-size:26px;font-weight:600;color:var(--navy);white-space:nowrap;overflow:hidden}
.card-desc{position:absolute;top:1586px;font-size:15px;line-height:24px;color:#333;overflow:hidden}
.dots{position:absolute;left:470px;top:1744px;display:flex;gap:17px}
.dots i{width:8px;height:8px;border-radius:50%;background:var(--pink);display:block}
.dots i:nth-child(2){background:var(--navy)}
.arrow{position:absolute;top:1734px;width:30px;height:30px;border-radius:50%;display:flex;align-items:center;justify-content:center}

/* benefits */
.benefits{position:absolute;left:0;top:1826px;width:1200px;height:780px;background:var(--dark);color:var(--white)}
.benefits .eyebrow{position:absolute;left:0;width:1200px;top:102px;text-align:center;color:var(--white);font-weight:500}
.benefits h2{position:absolute;left:0;width:1200px;top:130px;text-align:center;font-size:32px;font-weight:500}
.benefits h2 u{text-decoration-thickness:2px;text-underline-offset:6px}
.perk{position:absolute;top:2046px;width:264px;height:460px;padding:20px;color:var(--white)}
.perk.active{background:var(--white);color:var(--ink);border-radius:8px}
.perk .photo{position:relative;width:100%;height:224px;border-radius:8px}
.perk h3{margin-top:28px;font-size:26px;line-height:27px;font-weight:500;letter-spacing:-.5px}
.perk p{margin-top:16px;font-size:12.5px;line-height:21px}

/* subscribe */
.subscribe{position:absolute;left:54px;top:2658px;width:1092px;height:390px;border-radius:20px;background:linear-gradient(90deg,#8e9297,#b2b6ba 45%,#9a9ea3);overflow:hidden}
.subscribe h2{position:absolute;left:0;width:1092px;top:90px;text-align:center;font-size:52px;line-height:58px;font-weight:600;color:var(--white);letter-spacing:-1px}
.field{position:absolute;top:240px;height:56px;background:var(--white);font-size:16px;color:#777;padding-left:40px;display:flex;align-items:center}

/* dream */
.dream{position:absolute;left:0;top:3102px;width:1200px;height:332px;background:linear-gradient(100deg,#3b3d40,#8b8d90 45%,#c9cacb)}
.dream h2{position:absolute;left:0;width:1200px;top:104px;text-align:center;font-size:54px;font-weight:600;color:var(--white);letter-spacing:-1.5px}
.dream .btn{left:472px;top:182px;width:254px;height:56px;font-size:16px}

/* articles */
.art-head .eyebrow{position:absolute;left:124px;top:3490px;color:#333;font-weight:500}
.art-head h2{position:absolute;left:124px;top:3518px;font-size:26px;font-weight:500}
.post{position:absolute;border-radius:12px;overflow:hidden}
.post h3{position:absolute;left:28px;font-weight:500;letter-spacing:-.5px}
.pill{position:absolute;left:28px;height:24px;padding:0 10px;border:1.5px solid currentColor;border-radius:12px;font-size:11px;display:flex;align-items:center;gap:8px}

/* reviews */
.reviews{position:absolute;left:0;top:4104px;width:1200px;height:436px;background:var(--navy-band);color:var(--white)}
.reviews .eyebrow{position:absolute;left:0;width:1200px;top:56px;text-align:center;color:var(--white);font-weight:500}
.reviews h2{position:absolute;left:0;width:1200px;top:86px;text-align:center;font-size:34px;font-weight:600}
.reviews h2 a{color:var(--pink);text-underline-offset:6px}
.rate{position:absolute;top:182px;width:490px;height:204px;background:var(--white);color:var(--ink);overflow:hidden}
.rate .badge{position:absolute;left:-20px;top:60px;width:150px;height:150px;border-radius:50%}
.rate p{position:absolute;left:174px;top:22px;font-size:26px;line-height:31px;letter-spacing:-.5px}
.rate .score{position:absolute;left:174px;top:112px;font-size:32px;color:var(--navy);display:flex;gap:24px;align-items:center}
.rate .score span{font-size:24px}
.rate small{position:absolute;left:174px;top:162px;font-size:11px;display:flex;gap:10px}

/* contact */
.tile{position:absolute;top:4596px;width:242px;height:348px;border-radius:12px;color:var(--white);overflow:hidden}
.tile .inner{position:absolute;left:28px;bottom:36px}
.tile h3{font-size:26px;font-weight:500;margin-top:14px}
.tile p{font-size:12px;line-height:22px;margin-top:14px}
.app{position:absolute;left:880px;width:194px;height:166px;border-radius:12px;background:var(--navy);color:var(--white);display:flex;flex-direction:column;align-items:center;justify-content:center;gap:16px;font-size:11px}
.app b{font-size:16px;font-weight:500}
.app i{width:12px;height:12px;border-radius:50%;background:var(--white);display:block}

/* footer */
.foot-links{position:absolute;left:54px;top:5024px;display:flex;gap:22px;font-size:12px}
.foot-links a{color:#333;text-decoration:underline}
.social{position:absolute;top:5022px;width:22px;height:22px;border-radius:50%}
.copy{position:absolute;left:54px;top:5068px;font-size:11px;color:#333}
</style>
</head>
<body>

<header class="hero" role="img" aria-label="Smiling father carrying two young children outdoors">
  <div class="brand"><i></i>Brightwell</div>
  <div class="menu"><span></span><span></span><span></span></div>
  <h1>Finance, Property,<br>Conveyancing</h1>
  <p>Unlocking Opportunities and solving<br>problems.</p>
  <a class="btn">Chat Now
    <svg width="20" height="20" viewBox="0 0 20 20"><path d="M4 16L16 4M7 4h9v9" stroke="#fff" stroke-width="2.4" fill="none"/></svg></a>
</header>

<section class="svc">
  <div class="abs eyebrow" style="left:118px;top:872px;display:flex;gap:14px;align-items:center">
    <svg width="18" height="18" viewBox="0 0 18 18"><path d="M3 15l7-7M11 3a4 4 0 104 4l-2 0-2-2z" stroke="#0b3a6e" stroke-width="1.8" fill="none"/></svg>OUR SERVICE</div>
  <div class="svc-mark"><i></i><b>Brightwell</b></div>
  <h2>Unlocking Opportunities<br>and solving problems</h2>
  <div class="find">Find Here
    <svg width="16" height="14" viewBox="0 0 16 14"><path d="M1 7h13M9 2l5 5-5 5" stroke="#222" stroke-width="1.6" fill="none"/></svg></div>

  <div class="card-img photo" role="img" aria-label="Laptop showing finance charts" style="left:470px;width:250px;background:linear-gradient(160deg,#d9dcdd,#9aa2a5 60%,#565b5e)"></div>
  <div class="card-img photo" role="img" aria-label="Piggy bank beside model house on plans" style="left:746px;width:292px;background:linear-gradient(160deg,#e4e2df,#c6b6b0 50%,#8c8f93)"></div>
  <div class="card-img photo" role="img" aria-label="Row of colourful townhouses" style="left:1066px;width:70px;background:linear-gradient(180deg,#7f9fc8,#e0c14e 50%,#b9473a)"></div>

  <div class="card-title" style="left:470px;width:250px">ANCE</div>
  <div class="card-desc" style="left:470px;width:250px">ur home, car, investments, and<br>s</div>
  <div class="card-title" style="left:746px;width:292px">PROPERTY</div>
  <div class="card-desc" style="left:746px;width:292px">Sales, purchases, and rentals</div>
  <div class="card-title" style="left:1066px;width:70px">CONV</div>
  <div class="card-desc" style="left:1066px;width:70px;white-space:nowrap">For seam</div>

  <div class="dots"><i></i><i></i><i></i><i></i><i></i></div>
  <div class="arrow" style="left:1064px;background:var(--pink)"><svg width="14" height="12" viewBox="0 0 14 12"><path d="M13 6H2M6 1L1 6l5 5" stroke="#fff" stroke-width="1.8" fill="none"/></svg></div>
  <div class="arrow" style="left:1108px;background:var(--navy)"><svg width="14" height="12" viewBox="0 0 14 12"><path d="M1 6h11M8 1l5 5-5 5" stroke="#fff" stroke-width="1.8" fill="none"/></svg></div>
</section>

<section class="benefits">
  <div class="eyebrow">BENEFITS</div>
  <h2>WHY <u>BRIGHTWELL?</u></h2>
</section>
<div class="perk active" style="left:56px">
  <div class="photo" role="img" aria-label="Senior man in a cap among greenery" style="background:linear-gradient(160deg,#6f8a6a,#a6a7a3 50%,#4f5852)"></div>
  <h3>20 years<br>experience</h3>
  <p>We have grown and changed with the industry, and we're dedicated to continually improve our service and products so you get the best solutions possible.</p>
</div>
<div class="perk" style="left:330px">
  <div class="photo" role="img" aria-label="Signpost silhouette at sunset" style="background:linear-gradient(180deg,#7c8ba4,#b79aae 60%,#e5a0a7)"></div>
  <h3>We give you<br>choice</h3>
  <p>Working with over 20 large and small lenders, property developers and switched on accountants, we have the scope to give you good choices for the future.</p>
</div>
<div class="perk" style="left:605px">
  <div class="photo" role="img" aria-label="Laptop displaying charts" style="background:linear-gradient(160deg,#6c6f74,#c8cbd0 55%,#3a3c40)"></div>
  <h3>It is about the<br>outcome</h3>
  <p>When we say we care, we mean it. If you are a client now, we want you to be a happy client. If we cannot help you become a client today we'd like to help you tomorrow.</p>
</div>
<div class="perk" style="left:880px">
  <div class="photo" role="img" aria-label="Advisers reviewing documents at a laptop" style="background:linear-gradient(160deg,#9ba7aa,#dfe3e3 55%,#6d7678)"></div>
  <h3>Options that<br>makes sense</h3>
  <p>Our team of finance, property investment and accounting experts know what they are talking about, and they are happy to take the time to explain things clearly.</p>
</div>

<section class="subscribe" role="img" aria-label="Man in glasses smiling, grey backdrop">
  <h2>SUBSCRIBE TO KEEP UP TO<br>DATE ON MARKET NEWS</h2>
  <div class="field" style="left:122px;width:308px">Your Name</div>
  <div class="field" style="left:462px;width:300px">Input Your Email</div>
  <a class="btn" style="left:792px;top:240px;width:176px;height:56px;font-size:15px">Subscribe</a>
</section>

<section class="dream" role="img" aria-label="Man in a suit looking down, studio portrait">
  <h2>Your Dream, Our Team!</h2>
  <a class="btn">Meet Our Team
    <svg width="14" height="12" viewBox="0 0 14 12"><path d="M1 6h11M8 1l5 5-5 5" stroke="#fff" stroke-width="1.8" fill="none"/></svg></a>
</section>

<section class="art-head">
  <div class="eyebrow">ARTICLE</div>
  <h2>For Your Knowledge</h2>
  <a class="btn" style="left:880px;top:3490px;width:194px;height:58px;font-size:16px">View All
    <svg width="14" height="12" viewBox="0 0 14 12"><path d="M1 6h11M8 1l5 5-5 5" stroke="#fff" stroke-width="1.8" fill="none"/></svg></a>
</section>
<article class="post" style="left:124px;top:3588px;width:950px;height:248px;background:var(--yellow);color:var(--navy)">
  <div class="photo" role="img" aria-label="Surprised woman in a knitted beanie" style="left:330px;top:0;width:360px;height:248px;background:linear-gradient(180deg,#e9c85a,#d6b07a 50%,#eec96a)"></div>
  <h3 style="top:60px;font-size:26px;line-height:31px">Credit Scores -<br>What Are They<br>and How Do They<br>Affect Yout</h3>
  <div class="pill" style="top:198px">Read More <svg width="10" height="8" viewBox="0 0 10 8"><path d="M0 4h8M5 1l3 3-3 3" stroke="currentColor" stroke-width="1.4" fill="none"/></svg></div>
</article>
<article class="post" style="left:124px;top:3848px;width:470px;height:204px;background:linear-gradient(160deg,#a2322f,#c8c1b6 55%,#3f8f5a);color:var(--white)" role="img" aria-label="Credit rating report on a desk">
  <h3 style="top:76px;font-size:26px;line-height:30px">Poor Credit Home<br>Loan Refinance</h3>
  <div class="pill" style="top:150px">Read More <svg width="10" height="8" viewBox="0 0 10 8"><path d="M0 4h8M5 1l3 3-3 3" stroke="currentColor" stroke-width="1.4" fill="none"/></svg></div>
</article>
<article class="post" style="left:606px;top:3848px;width:468px;height:204px;background:linear-gradient(160deg,#7b8fa5,#c3ccd6 55%,#e4e6e9);color:var(--white)" role="img" aria-label="Person holding a tablet at a desk">
  <h3 style="top:76px;font-size:26px;line-height:30px">Understanding<br>Appraisals</h3>
  <div class="pill" style="top:150px">Read More <svg width="10" height="8" viewBox="0 0 10 8"><path d="M0 4h8M5 1l3 3-3 3" stroke="currentColor" stroke-width="1.4" fill="none"/></svg></div>
  <div class="abs" style="left:88px;top:186px;font-size:15px;font-weight:600;color:#1c1c1c">Understanding Appraisals</div>
</article>

<section class="reviews">
  <div class="eyebrow">REVIEWS</div>
  <h2>Read what our clients say <a>About us</a></h2>
  <div class="rate" style="left:100px">
    <div class="badge" style="background:#8cc63f"></div>
    <p>Rated 5.0 out 5 on<br>reviewhub.com.au</p>
    <div class="score">5.0 <span>★ ★ ★ ★ ★</span></div>
    <small>Read More <svg width="10" height="8" viewBox="0 0 10 8"><path d="M0 4h8M5 1l3 3-3 3" stroke="#222" stroke-width="1.4" fill="none"/></svg></small>
  </div>
  <div class="rate" style="left:610px">
    <div class="badge" style="background:#d9443a"></div>
    <p>Rated 4.9 out 5 on<br>Searchline Reviews</p>
    <div class="score">4.9 <span>★ ★ ★ ★ ★</span></div>
    <small>Read More <svg width="10" height="8" viewBox="0 0 10 8"><path d="M0 4h8M5 1l3 3-3 3" stroke="#222" stroke-width="1.4" fill="none"/></svg></small>
  </div>
</section>

<div class="tile" style="left:124px;background:linear-gradient(160deg,#7c6a5a,#a89482 50%,#3b342e)" role="img" aria-label="Smiling woman working at a laptop">
  <div class="inner">
    <svg width="40" height="40" viewBox="0 0 40 40"><circle cx="20" cy="20" r="17" stroke="#fff" stroke-width="1.6" fill="none"/><path d="M20 9v11l7 5" stroke="#fff" stroke-width="1.6" fill="none"/></svg>
    <h3>Opening Times</h3>
    <p>Monday – Friday: 9am-5pm<br>Saturday – Sunday: Closed</p>
  </div>
</div>
<div class="tile" style="left:376px;background:linear-gradient(160deg,#8d8a86,#bdb9b3 50%,#5a5753)" role="img" aria-label="Hand holding a phone handset">
  <div class="inner">
    <svg width="40" height="40" viewBox="0 0 40 40"><path d="M10 6l6 2 2 8-4 3c2 5 5 8 10 10l3-4 8 2 2 6c-2 3-5 4-8 3C18 33 8 23 5 12c-1-3 1-5 5-6z" stroke="#fff" stroke-width="1.6" fill="none"/></svg>
    <h3>Contact Us</h3>
    <p>info@brightwell.com.au<br>1300 418 275</p>
  </div>
</div>
<div class="tile" style="left:628px;background:linear-gradient(160deg,#8e9aa6,#b9c0c4 50%,#4f6a45)" role="img" aria-label="Suburban house with garden">
  <div class="inner">
    <svg width="40" height="40" viewBox="0 0 40 40"><path d="M4 10l10-4 12 4 10-4v24l-10 4-12-4-10 4zM14 6v24M26 10v24" stroke="#fff" stroke-width="1.6" fill="none"/></svg>
    <h3>Reach Us</h3>
    <p>24 Ashgrove Lane, Kelvin Park<br>VIC 3170</p>
  </div>
</div>
<div class="app" style="top:4596px"><b>Mobile</b>Get Mobile App<i></i></div>
<div class="app" style="top:4778px"><svg width="24" height="24" viewBox="0 0 24 24"><rect x="5" y="2" width="14" height="20" rx="3" fill="#fff"/></svg>Get Tablet App<i></i></div>

<footer>
  <nav class="foot-links">
    <a>HOME</a><a>WHY BRIGHTWELL</a><a>CONTACT US</a><a>PRIVACY POLICY</a><a>PRIVACY CONSENT &amp; CREDIT GUIDE</a><a>DISPUTE RESOLUTION</a>
  </nav>
  <span class="social" style="left:1046px;background:#e0322f"></span>
  <span class="social" style="left:1096px;background:#1877f2"></span>
  <div class="copy">© 2024 Larkspan Pty Ltd - All Rights Reserved - ABN: 47 219 530 816</div>
</footer>

</body>
</html>
```